3 Buttons for Web Site

Hi,

I need three images designed for a web site. They will be used as buttons. If you goto http://www.tarvenmetrix.ie/ you will see three image buttons on the home page. (One of man, one of a family and one of a woman). I need three identical sized buttons, one to have the text "BI Consultancy", one "Managed Near-Shore" and one "QDRX Performance" (Same font etc)

I am thinking of a jigsaw solution, where the text is the missing piece of a puzzle. The rest of the pieces are visible but faint in the background. I would like the back ground of the missing piece to be the same green that is used in the site logo. I attach a basic idea of what I am looking for. Forget about the hand and the piece held by the hand, it is the missing piece that I want the attention on, with some of the surrounding pieces.

I would like the design to blend with the general design of the rest of the site. I am happy to receive 1 PSD and I can do the other two buttons as I will just have to edit the text for those. NB - I use Photoshop elements, not full Photoshop, but that shouldn't make a difference.

I am open to an totally alternative design if you wish.

```html
<!DOCTYPE html>
<html lang="en">
<head>
<meta charset="utf-8">
<title>TarvenMetrix – Services</title>
<link href="https://fonts.googleapis.com/css2?family=Open+Sans:ital,wght@0,400;0,600;1,400&family=Tinos&display=swap" rel="stylesheet">
<style>
  :root {
    --page-bg: #e6e6e6;
    --band-bg: #dbdcdc;
    --slate: #5f6e72;
    --card-top: #ffffff;
    --card-bottom: #ededed;
    --text: #5a5a5a;
    --nav-text: #3c3c3c;
    --brand-green: #6aa22c;
    --white: #ffffff;
  }
  * { margin: 0; padding: 0; box-sizing: border-box; }
  html, body { width: 1200px; height: 622px; overflow: hidden; }
  body {
    position: relative;
    background: var(--page-bg);
    font-family: "Open Sans", Arial, sans-serif;
    color: var(--text);
  }
  .top-strip { position: absolute; left: 95px; top: 0; width: 1039px; height: 40px; background: var(--white); }
  .header-band { position: absolute; left: 0; top: 47px; width: 1200px; height: 90px; background: var(--band-bg); }
  .header-bar { position: absolute; left: 64px; top: 42px; width: 1100px; height: 99px; background: var(--slate); border-radius: 4px; }

  .card {
    position: absolute;
    background: linear-gradient(var(--card-top), var(--card-bottom));
    border-radius: 8px;
    box-shadow: 0 3px 10px rgba(0,0,0,.35);
  }
  .brand-card { left: 80px; top: 30px; width: 384px; height: 130px; display: flex; align-items: center; padding-left: 22px; gap: 12px; }
  .brand-mark { width: 20px; height: 20px; border-radius: 50%; background: var(--brand-green); }
  .brand-name { font-size: 38px; font-weight: 600; color: var(--brand-green); letter-spacing: -.5px; }

  .nav-card { left: 741px; top: 27px; width: 408px; height: 130px; display: flex; align-items: center; padding-left: 16px; }
  .nav-item { font-size: 13px; letter-spacing: 1px; color: var(--nav-text); padding: 0 16px; height: 98px; display: flex; align-items: center; }
  .nav-item.is-active { background: #ececec; border: 1px solid #dcdcdc; border-radius: 3px; }

  .intro { position: absolute; left: 0; top: 129px; width: 1230px; text-align: center; font-size: 16px; line-height: 26px; color: var(--text); }

  .service { position: absolute; top: 222px; width: 320px; text-align: center; }
  .service-art {
    display: block; margin: 0 auto; width: 180px; height: 180px; border-radius: 50%;
    background: radial-gradient(circle, #7aac3e 0 30%, #f4f4f4 31% 60%, rgba(230,230,230,0) 72%);
  }
  .service-text { margin-top: 26px; font-style: italic; font-size: 18px; line-height: 26px; color: var(--text); }
  .service-button {
    display: inline-block; margin-top: 16px; padding: 0 14px; height: 34px; line-height: 34px;
    background: var(--slate); color: var(--white); font-size: 16px; border-radius: 4px;
    border: 1px solid #4e5b5f;
  }
  .col-1 { left: 93px; }
  .col-2 { left: 452px; }
  .col-3 { left: 813px; }

  .footer-heading { position: absolute; top: 604px; font-family: "Tinos", "Times New Roman", serif; font-size: 22px; color: #555; }
</style>
</head>
<body>
  <div class="top-strip"></div>
  <div class="header-band"></div>
  <div class="header-bar"></div>

  <p class="intro">
    We provide expert Business Intelligence soloutions. We have been building on the<br>
    Corvane BI Platform since 1999. As well as on-site solutions, we offer remote working and managed near-shore development resouces.<br>
    We also offer technology independant BI startegy services to guide and assist BI teams with their BI Strategy and procedures.
  </p>

  <div class="card brand-card">
    <span class="brand-mark"></span>
    <span class="brand-name">TarvenMetrix</span>
  </div>

  <nav class="card nav-card">
    <span class="nav-item is-active">SERVICES</span>
    <span class="nav-item">CLIENTS</span>
    <span class="nav-item">CONTACT ME</span>
    <span class="nav-item">BLOG</span>
  </nav>

  <section class="service col-1">
    <span class="service-art" role="img" aria-label="Jigsaw puzzle with green missing piece labelled BI Consultancy"></span>
    <p class="service-text">With 15 years of experience in delivering Business Intelligence Solutions, you can be assured that we will deliver results.</p>
    <span class="service-button">BI Consultancy Services</span>
  </section>

  <section class="service col-2">
    <span class="service-art" role="img" aria-label="Jigsaw puzzle with green missing piece labelled Managed Near-Shore"></span>
    <p class="service-text">Combine the cost effectiveness of off-shore development with the quality of on-site design and management</p>
    <span class="service-button">Managed Near Shore</span>
  </section>

  <section class="service col-3">
    <span class="service-art" role="img" aria-label="Jigsaw puzzle with green missing piece labelled QDRX Performance"></span>
    <p class="service-text">Get more performance from your Cube Services investment. Our tuning solution gets the max from your environment.</p>
    <span class="service-button">QDRX Performance</span>
  </section>

  <h3 class="footer-heading" style="left:84px">Contact Details</h3>
  <h3 class="footer-heading" style="left:358px">Links</h3>
  <h3 class="footer-heading" style="left:634px">Local</h3>
</body>
</html>
```